Business Card Design Project

We need a business card design for a new company based in Singapore called 'Bright Harbor Pte Ltd'. We provide personal development training and emotional intelligence workshops. Our slogan is "Actualize your potentials". We will not have a company address on the business card. Only phone number, email address and website address.

Target Market(s)

Adults age 25 to 45 years old.
Mostly working in a job.

Industry/Entity Type

Training

Colors
0255a2
f37123

```html
<!DOCTYPE html>
<html lang="en">
<head>
<meta charset="utf-8">
<title>Bright Harbor – Business Card</title>
<link rel="stylesheet" href="https://fonts.googleapis.com/css2?family=Exo+2:wght@400;600;700&family=Archivo+Black&display=swap">
<style>
  :root {
    --backdrop: #ebe7e1;
    --white: #ffffff;
    --brand-blue: #0d73c9;
    --blue-light: #2f9ae6;
    --blue-deep: #0255a2;
    --blue-navy: #1d3f8f;
    --orange: #f37123;
    --silver: #c9ccd1;
    --ink: #1d1d1d;
    --ink-soft: #333333;
  }
  * { margin: 0; padding: 0; box-sizing: border-box; }
  html, body { width: 1200px; height: 1050px; overflow: hidden; }
  body {
    background: var(--backdrop);
    font-family: "Exo 2", sans-serif;
    position: relative;
  }
  .card {
    position: absolute;
    top: 157px;
    width: 420px;
    height: 735px;
    overflow: hidden;
    background: var(--white);
    box-shadow: 0 10px 30px rgba(0,0,0,0.18);
  }
  .card--front { left: 150px; }
  .card--back { left: 630px; }

  /* front */
  .front__top-band {
    position: absolute; top: 0; left: 0; right: 0; height: 12px;
    background: var(--brand-blue);
  }
  .brand {
    position: absolute; top: 44px; left: 40px;
    display: flex; align-items: center; gap: 14px;
  }
  .brand__dot {
    width: 58px; height: 58px; border-radius: 50%;
    background: var(--blue-light);
  }
  .brand__name {
    font-weight: 600; font-size: 38px; color: var(--brand-blue);
    letter-spacing: 0.5px;
  }
  .front__divider {
    position: absolute; top: 148px; left: 0; right: 0; height: 16px;
    background: var(--blue-navy);
  }
  .front__body {
    position: absolute; top: 164px; left: 0; right: 0; height: 484px;
    background: radial-gradient(ellipse at 60% 40%, var(--blue-light) 0%, var(--brand-blue) 60%, var(--blue-deep) 100%);
  }
  .connector { position: absolute; top: 0; left: 0; }
  .name-plate {
    position: absolute; top: 22px; left: 178px; width: 222px; height: 82px;
    background: var(--white);
    padding: 14px 12px;
    text-align: center;
  }
  .name-plate__name {
    font-family: "Archivo Black", sans-serif;
    font-size: 22px; color: var(--ink); letter-spacing: 0.5px;
  }
  .name-plate__role {
    font-size: 14px; color: var(--ink-soft); margin-top: 4px;
  }
  .contact {
    position: absolute; width: 270px; height: 78px;
    border: 2px solid var(--white);
    color: var(--white); text-align: center;
    padding-top: 14px;
  }
  .contact--phone { top: 128px; left: 130px; }
  .contact--email { top: 234px; left: 100px; }
  .contact--web { top: 340px; left: 62px; }
  .contact__label { font-weight: 700; font-size: 18px; letter-spacing: 1px; }
  .contact__value { font-size: 15px; margin-top: 4px; letter-spacing: 0.5px; }
  .front__rule {
    position: absolute; top: 648px; left: 0; right: 0; height: 8px;
    background: linear-gradient(var(--silver), #8e939a);
  }
  .front__footer {
    position: absolute; top: 656px; left: 0; right: 0; bottom: 0;
    background: var(--orange);
    color: var(--white);
    display: flex; align-items: center; justify-content: center;
    font-size: 20px; font-weight: 600; letter-spacing: 0.5px;
  }

  /* back */
  .back__divider {
    position: absolute; top: 420px; left: 0; right: 0; height: 14px;
    background: var(--blue-navy);
  }
  .back__body {
    position: absolute; top: 434px; left: 0; right: 0; bottom: 0;
    background: radial-gradient(ellipse at 40% 40%, var(--blue-light) 0%, var(--brand-blue) 55%, var(--blue-navy) 100%);
    color: var(--white);
    padding: 70px 40px 0;
  }
  .back__slogan {
    font-size: 26px; font-weight: 600; line-height: 1.5; letter-spacing: 0.5px;
  }
</style>
</head>
<body>
  <section class="card card--front">
    <div class="front__top-band"></div>
    <div class="brand">
      <span class="brand__dot"></span>
      <span class="brand__name">Bright Harbor</span>
    </div>
    <div class="front__divider"></div>
    <div class="front__body">
      <svg class="connector" width="420" height="484" viewBox="0 0 420 484" fill="none" stroke="#ffffff" stroke-width="2">
        <path d="M178 26 H60 V380 H62"/>
        <path d="M60 90 H178"/>
        <path d="M60 166 H130"/>
        <path d="M60 272 H100"/>
      </svg>
      <div class="name-plate">
        <div class="name-plate__name">DANIEL REYES</div>
        <div class="name-plate__role">Managing Director</div>
      </div>
      <div class="contact contact--phone">
        <div class="contact__label">PHONE</div>
        <div class="contact__value">012 555 0147</div>
      </div>
      <div class="contact contact--email">
        <div class="contact__label">EMAIL</div>
        <div class="contact__value">hello@brightharbor.sg</div>
      </div>
      <div class="contact contact--web">
        <div class="contact__label">WEBSITE</div>
        <div class="contact__value">www.brightharbor.sg</div>
      </div>
    </div>
    <div class="front__rule"></div>
    <div class="front__footer">Actualize your potentials</div>
  </section>

  <section class="card card--back">
    <div class="back__divider"></div>
    <div class="back__body">
      <p class="back__slogan">Actualize your<br>potentials</p>
    </div>
  </section>
</body>
</html>
```